Solmira Full Spectrum CBD Oil infused with turmeric, black pepper and cacao extracts

Using company logo attached, dosage info attached, NHC disclaimer attached, pharmacist disclaimer below, ingredient list below and bar code.
Above "Full Spectrum" part of the logo I would like "Solmira" in hand written font and in light green color close to the logo color. White background color please. The smaller logos that were attached in the file need to be on the back side of the label with the ingridients list to the right of the logo in and the disclaimers to the left of it.

Requirements
Must have
• -ORGANIC
• -USA GROWN
• -30mL
• -1500MG CBD
• -This product is not approved by NHC for the diagnosis, cure, mitigation, treatment, or prevention of any disease. Please consult with your physician or pharmacist before using CBD if you are taking medication of any kind.
• -Directions: Administer 5 drops sublingually 2-3 times per day or as needed. Hold under your tongue for 60 seconds then swallow.
• -Ingredients: Organic MCT Oil, Organic Hemp Extract, proprietary organic terpene blend, Organic Hemp derived minerals

```html
<!DOCTYPE html>
<html lang="en">
<head>
<meta charset="utf-8">
<title>Solmira Full Spectrum – Label</title>
<link href="https://fonts.googleapis.com/css2?family=Great+Vibes&family=Quicksand:wght@500;600&family=Roboto:wght@300;400&display=swap" rel="stylesheet">
<style>
  :root{
    --bg:#aeafa5;
    --label-white:#ffffff;
    --mist:#e9eef2;
    --brand-green:#168a3c;
    --script-green:#7cc242;
    --ink:#111111;
    --drop-blue:#2b9be0;
  }
  html,body{margin:0;padding:0;width:1200px;height:942px;overflow:hidden;background:var(--bg);}
  .label{
    position:absolute;left:261px;top:44px;width:677px;height:854px;
    background:var(--brand-green);box-shadow:0 2px 6px rgba(0,0,0,.18);overflow:hidden;
  }
  .label__top{
    position:absolute;left:0;top:0;width:100%;height:421px;
    background:radial-gradient(ellipse at 50% 45%, var(--label-white) 0%, var(--label-white) 45%, var(--mist) 100%);
  }
  .brand-script{
    position:absolute;left:0;right:0;top:26px;text-align:center;
    font-family:"Great Vibes",cursive;font-size:50px;color:var(--script-green);line-height:1;
    padding-left:10px;
  }
  .product-line{
    position:absolute;left:0;right:0;top:95px;margin:0;text-align:center;
    font-family:"Quicksand",sans-serif;font-weight:600;font-size:44px;color:var(--ink);line-height:1;
  }
  .brand-mark{
    position:absolute;left:0;right:0;top:225px;display:flex;justify-content:center;align-items:center;gap:12px;
    font-family:"Quicksand",sans-serif;font-weight:600;font-size:36px;color:var(--brand-green);line-height:1;
  }
  .brand-mark__dot{width:22px;height:22px;border-radius:50%;background:var(--brand-green);}
  .tagline{
    position:absolute;left:0;right:0;top:349px;text-align:center;
    font-family:"Quicksand",sans-serif;font-weight:500;font-size:36px;color:var(--ink);line-height:1;
  }
  .organic-box{
    position:absolute;left:73px;top:446px;width:529px;height:64px;border:3px solid var(--label-white);
    display:flex;align-items:center;justify-content:center;
    font-family:"Roboto",sans-serif;font-weight:300;font-size:46px;color:var(--label-white);
  }
  .facts{font-family:"Roboto",sans-serif;color:var(--label-white);}
  .facts__disclaimer{
    position:absolute;left:30px;top:590px;width:176px;height:142px;margin:0;
    display:flex;align-items:center;
    font-size:14px;line-height:19px;font-weight:400;
  }
  .facts__divider{position:absolute;top:590px;width:3px;height:142px;background:var(--label-white);}
  .facts__origin{position:absolute;left:217px;width:242px;top:642px;text-align:center;font-size:32px;font-weight:300;line-height:1.2;}
  .facts__dose{position:absolute;left:462px;width:212px;top:642px;text-align:center;font-size:32px;font-weight:300;line-height:1.2;}
  .volume{
    position:absolute;left:273px;top:788px;width:138px;height:45px;background:var(--label-white);
    display:flex;align-items:center;justify-content:center;
    font-family:"Roboto",sans-serif;font-size:29px;color:var(--ink);
  }
  .volume svg{margin-left:2px;margin-top:-16px;}
</style>
</head>
<body>
  <main class="label">
    <section class="label__top" role="img" aria-label="Field of clear water droplets on white"></section>
    <div class="brand-script">Solmira</div>
    <h1 class="product-line">FULL SPECTRUM</h1>
    <div class="brand-mark"><span class="brand-mark__dot"></span>SOLMIRA</div>
    <div class="tagline">HOLISTIC HEALING</div>

    <div class="organic-box">ORGANIC HEMP</div>

    <div class="facts">
      <p class="facts__disclaimer">This product is not approved by NHC for the diagnosis, cure, mitigation, treatment, or prevention of any disease.</p>
      <span class="facts__divider" style="left:214px"></span>
      <div class="facts__origin">USA GROWN</div>
      <span class="facts__divider" style="left:459px"></span>
      <div class="facts__dose">1500MG CBD</div>
    </div>

    <div class="volume">30ml<svg width="8" height="12" viewBox="0 0 8 12"><path d="M4 0 C4 0 0 6 0 8 A4 4 0 0 0 8 8 C8 6 4 0 4 0Z" fill="var(--drop-blue)"/></svg></div>
  </main>
</body>
</html>
```